Private launch of Lunet, the smart baby sleep tracker

We need a webpage/website to initiate the Private launch of Lunet, our baby sleep tracker.

Meet Lunet:
Sleep, or rather the lack of sleep, is the one of the most challenging aspect of caring for a newborn in the first year. Recently, phone apps for baby tracking have taken hold. But those continue requiring parents to manually enter sleep and awake time. Sleep-deprived parents need a safe, automatic, accurate and stress-free tracking system. Therefore, we provide an affordable smart wearable to track baby’s sleep based on baby’s vital signs.

Target Market(s)

new parents with infants

Industry/Entity Type

Baby Care

Number of Pages Required

1 page

Font styles to use
Sans Serif

Colors
85cae6
f8ba93

Requirements
Must have
• Lunet baby sleep tracker, demonstration video, payment and ordering information. Introduction of our company "Corvane Tesk Digital".
• Considering the primary targets are sleep-deprived new parents, the webpage should be user-friendly.
Nice to have
• Product rating and reviews

```html
<!DOCTYPE html>
<html lang="en">
<head>
<meta charset="utf-8">
<title>Lunet — Smart Baby Sleep Tracker</title>
<link href="https://fonts.googleapis.com/css2?family=Montserrat:wght@300;400;500;600;700&family=Open+Sans:wght@400;600&display=swap" rel="stylesheet">
<style>
:root{
  --blue:#85cae6;
  --blue-deep:#5fb6da;
  --peach:#f8ba93;
  --peach-deep:#f4a271;
  --ink:#2f3a44;
  --text:#6b7278;
  --muted:#9aa1a6;
  --pale:#eef7fb;
  --dark:#3c4550;
  --white:#ffffff;
  --skin:#e8cbb8;
  --blanket:#efedeb;
}
*{box-sizing:border-box;margin:0;padding:0}
html,body{width:1200px;height:5373px;overflow:hidden}
body{font-family:"Open Sans",Arial,sans-serif;color:var(--text);background:var(--white);position:relative}
h1,h2,h3,h4,.nav,.btn,.stat-value{font-family:"Montserrat",Helvetica,sans-serif}
.accent{color:var(--peach)}
.btn{display:inline-block;border-radius:30px;font-size:14px;font-weight:600;color:var(--white);padding:12px 30px;text-decoration:none}
.btn-peach{background:var(--peach)}
.btn-blue{background:var(--blue)}
.section{position:absolute;left:0;width:1200px}
.ph{position:absolute}

/* hero */
.hero{top:0;height:730px;background:var(--blanket);overflow:hidden}
.hero-photo{left:0;top:0;width:1200px;height:730px;background:
  radial-gradient(ellipse 300px 260px at 860px 250px,#edc9b2 0%,#e9cdbb 55%,rgba(233,205,187,0) 100%),
  radial-gradient(ellipse 220px 150px at 1000px 500px,#e2c2ad 0%,rgba(226,194,173,0) 100%),
  linear-gradient(100deg,#f4f3f2 0%,#efedeb 40%,#e3dcd7 70%,#d8ccc3 100%)}
.nav{position:absolute;top:44px;left:80px;right:80px;display:flex;align-items:center}
.brand{display:flex;align-items:center;gap:10px;font-family:"Montserrat",sans-serif;font-weight:700;font-size:34px;color:var(--ink)}
.brand-dot{width:22px;height:22px;border-radius:50%;background:var(--peach)}
.nav-links{display:flex;gap:36px;margin-left:auto;margin-right:44px;font-size:15px;color:var(--ink)}
.nav-phone{display:flex;align-items:center;gap:8px}
.hero-title{position:absolute;left:80px;top:262px;font-size:52px;font-weight:300;color:var(--ink);line-height:1.2}
.hero-title b{font-weight:500}
.hero-sub{position:absolute;left:82px;top:395px;width:400px;font-size:16px;line-height:1.55;color:var(--ink)}
.hero-cta{position:absolute;left:82px;top:480px;display:flex;align-items:center;gap:22px}
.play{width:52px;height:52px;border-radius:50%;background:var(--white);display:flex;align-items:center;justify-content:center;box-shadow:0 2px 8px rgba(0,0,0,.08)}

/* benefit band */
.band{top:730px;height:212px;background:var(--blue)}
.band-items{display:flex;justify-content:center;gap:50px;padding-top:70px}
.band-item{width:150px;text-align:center;color:var(--white);font-size:13px;line-height:1.4}
.band-item svg{display:block;margin:0 auto 10px}
.band-btn{position:absolute;left:50%;top:922px;transform:translateX(-50%);border:2px solid var(--white);z-index:2}

/* what is */
.what{top:967px;height:745px}
.sec-title{text-align:center;font-size:36px;font-weight:600;color:var(--ink)}
.sec-sub{text-align:center;font-size:15px;margin-top:6px}
.what .sec-title{margin-top:60px}
.what-cols{position:absolute;top:160px;left:0;width:1200px;display:flex;justify-content:center;gap:260px}
.what-col{width:320px;text-align:center}
.circle{width:270px;height:270px;border-radius:50%;background:var(--peach);margin:0 auto;position:relative;overflow:hidden}
.what-col h3{font-size:20px;font-weight:600;color:var(--ink);margin-top:30px}
.what-col p{font-size:14px;line-height:1.6;margin-top:12px}
.what-col .btn{margin-top:26px;font-size:13px;padding:10px 28px}
.amp{position:absolute;left:556px;top:300px;width:86px;height:86px}

/* why */
.why{top:1712px;height:660px;background:var(--pale)}
.why .sec-title{margin-top:60px}
.why-photo{left:90px;top:130px;width:420px;height:265px;background:
  radial-gradient(ellipse 90px 100px at 130px 140px,#f2d9c8 0%,rgba(242,217,200,0) 100%),
  radial-gradient(ellipse 110px 120px at 300px 130px,#e6c2aa 0%,rgba(230,194,170,0) 100%),
  linear-gradient(100deg,#f4ebe4 0%,#ecd9cb 50%,#d9bca8 100%)}
.why-list{position:absolute;left:690px;top:160px;width:420px;list-style:none}
.why-list li{display:flex;gap:16px;font-size:15px;line-height:1.6;margin-bottom:26px}
.why-list svg{flex:0 0 auto;margin-top:4px}
.stats{position:absolute;left:125px;top:440px;width:950px;display:flex}
.stat{flex:1;text-align:center;border-right:1px solid #d3dde2}
.stat:last-child{border-right:0}
.stat-value{font-size:32px;font-weight:400;color:var(--ink)}
.stat-value.price{color:var(--peach)}
.stat-label{font-size:13px;margin-top:2px}
.why .btn{position:absolute;left:50%;transform:translateX(-50%);top:550px}

/* steps */
.steps{top:2372px;height:558px;background:var(--white);overflow:hidden}
.steps-photo{left:300px;top:120px;width:600px;height:330px;border-radius:0 0 40px 40px;background:
  radial-gradient(ellipse 130px 110px at 140px 230px,#f0d6c5 0%,rgba(240,214,197,0) 100%),
  radial-gradient(ellipse 130px 110px at 460px 230px,#f0d6c5 0%,rgba(240,214,197,0) 100%),
  linear-gradient(180deg,#d9dbe0 0%,#e6e3e2 30%,#f1e7e1 60%,#f7f1ed 100%)}
.steps .sec-title{position:relative;margin-top:52px;line-height:1.35}
.arrow{position:absolute;top:262px}
.step-row{position:absolute;left:0;width:1200px;top:470px;display:flex;justify-content:center;gap:60px}
.step{display:flex;align-items:center;gap:14px;width:290px;font-size:14px;line-height:1.45;color:var(--ink)}
.step-num{width:40px;height:40px;border-radius:50%;background:var(--blue);color:var(--white);display:flex;align-items:center;justify-content:center;font-weight:600;flex:0 0 auto;font-family:"Montserrat",sans-serif}

/* features */
.features{top:2930px;height:724px;background:var(--blue)}
.features .sec-title{margin-top:60px;line-height:1.35}
.feat-col{position:absolute;top:230px;width:380px}
.feat-left{left:90px}
.feat-right{left:730px}
.feat{display:flex;align-items:center;gap:18px;margin-bottom:72px}
.feat-left .feat{flex-direction:row-reverse;text-align:right}
.feat-icon{width:56px;height:56px;border-radius:50%;border:2px solid var(--white);display:flex;align-items:center;justify-content:center;flex:0 0 auto}
.feat h4{font-size:15px;font-weight:600;color:var(--white)}
.feat p{font-size:12px;color:#f2f9fc;margin-top:4px;line-height:1.45}
.phone{position:absolute;left:478px;top:170px;width:244px;height:470px;background:var(--white);border-radius:32px;box-shadow:0 10px 30px rgba(0,0,0,.12);padding:46px 14px}
.phone-screen{background:#f7fbfd;height:100%;border:1px solid #e2edf2;border-radius:4px;padding:10px;font-size:9px;color:var(--ink)}
.screen-head{text-align:center;font-weight:600;font-size:10px}
.screen-tabs{display:flex;justify-content:space-around;margin-top:8px;color:var(--muted)}
.screen-tabs span.on{color:var(--white);background:var(--blue);padding:1px 6px;border-radius:6px}
.screen-card{background:var(--white);border-radius:6px;margin-top:10px;padding:10px;text-align:center;font-size:9px;line-height:1.4;box-shadow:0 1px 4px rgba(0,0,0,.06)}
.avatar{width:30px;height:30px;border-radius:50%;background:var(--blue);margin:0 auto 6px}
.screen-row{display:flex;justify-content:space-between;margin-top:10px;font-weight:600}

/* video */
.video{top:3654px;height:536px;overflow:hidden}
.video-photo{left:0;top:0;width:1200px;height:536px;background:
  radial-gradient(ellipse 200px 120px at 380px 130px,#eed8ca 0%,rgba(238,216,202,0) 100%),
  radial-gradient(ellipse 260px 200px at 960px 200px,#e7cdbd 0%,rgba(231,205,189,0) 100%),
  linear-gradient(100deg,#f1f3f5 0%,#e7ebef 40%,#cfd8e0 70%,#bcc7d1 100%)}
.video-title{position:absolute;left:170px;top:205px;font-size:54px;font-weight:300;color:#5d6670;line-height:1.1}
.video-sub{position:absolute;left:172px;top:272px;font-size:30px;font-weight:300;color:#6d757d;line-height:1.3;font-family:"Montserrat",sans-serif;width:520px}
.video .cta{position:absolute;left:172px;top:390px;display:flex;align-items:center}
.video .play{width:54px;height:54px;background:var(--blue);margin-right:-20px;position:relative;z-index:1}
.video .btn{padding-left:36px}

/* get */
.get{top:4190px;height:280px}
.get-band{position:absolute;left:0;top:0;width:1200px;height:190px;background:var(--peach)}
.get .sec-title{position:relative;margin-top:62px;color:var(--ink)}
.get .accent{color:var(--white)}
.get .sec-sub{position:relative;color:var(--ink)}
.get .btn{position:absolute;left:50%;transform:translateX(-50%);top:166px;border:2px solid var(--white)}

/* about */
.about{top:4470px;height:509px}
.about-photo{left:40px;top:20px;width:560px;height:470px;border-radius:8px;background:
  radial-gradient(ellipse 150px 130px at 340px 150px,#f1d9cc 0%,rgba(241,217,204,0) 100%),
  radial-gradient(ellipse 150px 150px at 190px 320px,#c9cbcf 0%,rgba(201,203,207,0) 100%),
  linear-gradient(160deg,#f6eff0 0%,#eee3e4 50%,#e8e6e8 100%)}
.about-text{position:absolute;left:706px;top:150px;width:400px}
.about-text h2{font-size:30px;font-weight:600;color:var(--ink)}
.about-text p{font-size:15px;line-height:1.6;margin-top:14px}
.about-text .btn{margin-top:26px;font-size:13px;padding:10px 32px}

/* footer */
.footer{top:4979px;height:394px;background:var(--dark);color:#c4cad0;font-size:14px}
.foot-cols{position:absolute;top:64px;left:170px;display:flex}
.foot-col{width:300px;line-height:2}
.foot-col:nth-child(2){width:265px}
.foot-col:nth-child(3){width:235px}
.foot-contact .phone-line{color:var(--white);font-family:"Montserrat",sans-serif}
.social{display:flex;gap:10px;margin-top:10px}
.social span{width:26px;height:26px;border-radius:50%;background:var(--blue)}
.foot-bottom{position:absolute;left:170px;right:100px;top:318px;border-top:1px solid #525c66;padding-top:16px;display:flex;font-size:12px}
.foot-bottom .legal{margin-left:auto;margin-right:130px;display:flex;gap:22px}
</style>
</head>
<body>

<header class="section hero">
  <div class="ph hero-photo" role="img" aria-label="Photo of a sleeping newborn wearing the Lunet band on one leg, wrapped in a soft white blanket"></div>
  <nav class="nav">
    <div class="brand"><span class="brand-dot"></span>Lunet</div>
    <div class="nav-links">
      <span>Company</span><span>Product</span><span>Features</span><span>Contact</span>
      <span class="nav-phone"><svg width="14" height="14" viewBox="0 0 24 24"><path d="M6.6 10.8a15 15 0 0 0 6.6 6.6l2.2-2.2c.3-.3.7-.4 1-.2 1.1.4 2.3.6 3.6.6.6 0 1 .4 1 1V20c0 .6-.4 1-1 1C10.6 21 3 13.4 3 4c0-.6.4-1 1-1h3.5c.6 0 1 .4 1 1 0 1.3.2 2.5.6 3.6.1.3 0 .7-.2 1z" fill="#2f3a44"/></svg>1-800-555-0142</span>
    </div>
    <a class="btn btn-peach">Buy Now!</a>
  </nav>
  <h1 class="hero-title">Meet <b>Lu<span class="accent">net</span></b><br>Smart Sleep.</h1>
  <p class="hero-sub">A complete baby monitoring system with expert sleep guidance at your fingertips.</p>
  <div class="hero-cta">
    <span class="play"><svg width="16" height="18" viewBox="0 0 16 18"><path d="M2 1l13 8-13 8z" fill="#85cae6"/></svg></span>
    <a class="btn btn-peach">Buy Lunet</a>
  </div>
</header>

<section class="section band">
  <div class="band-items">
    <div class="band-item"><svg width="26" height="24" viewBox="0 0 24 22"><path d="M12 21L2.5 11.5A5.5 5.5 0 0 1 12 4a5.5 5.5 0 0 1 9.5 7.5z" fill="#fff"/></svg>Track heart rate and oxygen levels while your baby sleeps</div>
    <div class="band-item"><svg width="24" height="24" viewBox="0 0 24 24"><path d="M20 14A8 8 0 1 1 10 4a6.5 6.5 0 0 0 10 10z" fill="#fff"/></svg>See how long and how well baby slept</div>
    <div class="band-item"><svg width="28" height="22" viewBox="0 0 28 20"><rect x="1" y="3" width="18" height="14" rx="2" fill="#fff"/><path d="M20 8l7-4v12l-7-4z" fill="#fff"/></svg>Stream HD video and sound</div>
    <div class="band-item"><svg width="24" height="24" viewBox="0 0 24 24"><path d="M12 22a2.5 2.5 0 0 0 2.5-2.5h-5A2.5 2.5 0 0 0 12 22zm7-6V11a7 7 0 0 0-5.5-6.8V3a1.5 1.5 0 0 0-3 0v1.2A7 7 0 0 0 5 11v5l-2 2v1h18v-1z" fill="#fff"/></svg>Receive real-time notifications and insights</div>
  </div>
</section>
<a class="btn btn-blue band-btn">Learn More</a>

<section class="section what">
  <h2 class="sec-title">What is Lu<span class="accent">net</span>.</h2>
  <p class="sec-sub">Simplify infant sleep with AI</p>
  <div class="what-cols">
    <div class="what-col">
      <div class="circle"><div class="ph" role="img" aria-label="Hand holding the small white Lunet sensor" style="left:0;top:60px;width:270px;height:150px;background:linear-gradient(90deg,#f5d6c2 0%,#fbeee5 45%,#ffffff 70%,#f1e3d9 100%)"></div></div>
      <h3>Simplify infant sleep with AI</h3>
      <p>Lorem ipsum dolor consectetur adipiscing elit, sed do eiusmod tempor incididunt ut labore et dolore magna aliqua. Ut enim ad minim veniam, quis nostrud exercitation.</p>
      <a class="btn btn-blue">Learn More</a>
    </div>
    <div class="what-col">
      <div class="circle"><div class="ph" style="left:70px;top:30px;width:130px;height:250px;border-radius:16px;background:#fff;padding:18px 10px;font-size:8px;color:#2f3a44;text-align:center;line-height:1.35"><div class="avatar" style="width:26px;height:26px;margin-bottom:5px"></div>Baby's sleep score improved this week<div style="margin-top:10px;display:flex;justify-content:space-between;font-weight:600"><span>April</span><span>Hours</span></div><div style="margin-top:8px;height:50px;background:linear-gradient(90deg,#85cae6 0 8%,transparent 8% 16%,#85cae6 16% 24%,transparent 24% 32%,#85cae6 32% 40%,transparent 40% 48%,#85cae6 48% 56%,transparent 56% 64%,#85cae6 64% 72%,transparent 72% 80%,#85cae6 80% 88%,transparent 88%)"></div></div></div>
      <h3>A Phone &amp; Tablet App</h3>
      <p>Lorem ipsum dolor consectetur adipiscing elit, sed do eiusmod tempor incididunt ut labore et dolore magna aliqua. Ut enim ad minim veniam, quis nostrud exercitation.</p>
      <a class="btn btn-blue">Learn More</a>
    </div>
  </div>
  <svg class="amp" viewBox="0 0 76 76"><circle cx="30" cy="44" r="24" fill="none" stroke="#f8ba93" stroke-width="2"/><text x="30" y="53" text-anchor="middle" font-family="Montserrat,sans-serif" font-size="26" fill="#f8ba93">&amp;</text><circle cx="56" cy="20" r="14" fill="#fff" stroke="#85cae6" stroke-width="2"/><path d="M50 20h12M56 14v12" stroke="#85cae6" stroke-width="2"/></svg>
</section>

<section class="section why">
  <h2 class="sec-title">Why Lu<span class="accent">net</span>.</h2>
  <div class="ph why-photo" role="img" aria-label="Photo of a smiling mother holding her baby face to face"></div>
  <ul class="why-list">
    <li><svg width="16" height="14" viewBox="0 0 16 14"><path d="M1 7l5 5L15 1" fill="none" stroke="#f8ba93" stroke-width="2.4"/></svg>Alerts you if your baby stops breathing, rolls on his or her stomach or falls.</li>
    <li><svg width="16" height="14" viewBox="0 0 16 14"><path d="M1 7l5 5L15 1" fill="none" stroke="#f8ba93" stroke-width="2.4"/></svg>Universal form factor. Any onesie or pyjama works. Use it as your child grows!</li>
    <li><svg width="16" height="14" viewBox="0 0 16 14"><path d="M1 7l5 5L15 1" fill="none" stroke="#f8ba93" stroke-width="2.4"/></svg>The best flexibility, features and most affordable price of any wearable baby monitor.</li>
  </ul>
  <div class="stats">
    <div class="stat"><div class="stat-value price">$299.00</div><div class="stat-label">In stock</div></div>
    <div class="stat"><div class="stat-value">Free US</div><div class="stat-label">Shipping</div></div>
    <div class="stat"><div class="stat-value">90 Day</div><div class="stat-label">Return</div></div>
    <div class="stat"><div class="stat-value">1 Year</div><div class="stat-label">Warranty</div></div>
  </div>
  <a class="btn btn-peach">Buy Lunet</a>
</section>

<section class="section steps">
  <div class="ph steps-photo" role="img" aria-label="Photo of a baby's legs and feet in striped leggings resting on a white blanket"></div>
  <h2 class="sec-title">Just 3 Easy Steps to use the<br>Lu<span class="accent">net</span> Tracker.</h2>
  <svg class="arrow" style="left:84px" width="14" height="24" viewBox="0 0 14 24"><path d="M12 2L2 12l10 10" fill="none" stroke="#85cae6" stroke-width="2.5"/></svg>
  <svg class="arrow" style="right:84px" width="14" height="24" viewBox="0 0 14 24"><path d="M2 2l10 10L2 22" fill="none" stroke="#85cae6" stroke-width="2.5"/></svg>
  <div class="step-row">
    <div class="step"><span class="step-num">1</span>Clip Lunet to your baby's leg or hand.</div>
    <div class="step"><span class="step-num">2</span>Connect Lunet to your phone or tablet.</div>
    <div class="step"><span class="step-num">3</span>Monitor your baby in real time while sleep.</div>
  </div>
</section>

<section class="section features">
  <h2 class="sec-title">Feature of Lu<span class="accent" style="color:#fff">net</span> Tracker<br>Device and the App</h2>
  <div class="feat-col feat-left">
    <div class="feat"><span class="feat-icon"><svg width="26" height="20" viewBox="0 0 26 20"><circle cx="6" cy="8" r="3" fill="#fff"/><rect x="11" y="6" width="13" height="5" rx="2" fill="#fff"/><rect x="2" y="13" width="22" height="3" fill="#fff"/></svg></span><div><h4>Sleep Position Alarm</h4><p>Lorem ipsum is simply dummy text of the printing and typesetting</p></div></div>
    <div class="feat"><span class="feat-icon"><svg width="24" height="24" viewBox="0 0 24 24"><circle cx="12" cy="13" r="8" fill="none" stroke="#fff" stroke-width="2"/><path d="M12 9v4l3 2M4 4l3-2M20 4l-3-2" stroke="#fff" stroke-width="2" fill="none"/></svg></span><div><h4>Proximity Alarm</h4><p>Lorem ipsum is simply dummy text of the printing and typesetting</p></div></div>
    <div class="feat"><span class="feat-icon"><svg width="22" height="20" viewBox="0 0 22 20"><rect x="2" y="10" width="4" height="9" fill="#fff"/><rect x="9" y="4" width="4" height="15" fill="#fff"/><rect x="16" y="7" width="4" height="12" fill="#fff"/></svg></span><div><h4>Real-time stats</h4><p>Lorem ipsum is simply dummy text of the printing and typesetting</p></div></div>
  </div>
  <div class="phone">
    <div class="phone-screen">
      <div class="screen-head">Baby's Sleep</div>
      <div class="screen-tabs"><span>Day</span><span>Week</span><span class="on">Month</span></div>
      <div class="screen-card"><div class="avatar"></div>Baby's sleep score increased 20% lately, she is sleeping deeper!</div>
      <div class="screen-row"><span>April 2018</span><span>Sleep Hours</span></div>
      <svg width="190" height="120" viewBox="0 0 190 120" style="margin-top:10px">
        <line x1="0" y1="110" x2="190" y2="110" stroke="#d7e6ec"/>
        <g fill="#85cae6">
          <rect x="4" y="50" width="6" height="60"/><rect x="16" y="30" width="6" height="80"/><rect x="28" y="62" width="6" height="48"/><rect x="40" y="40" width="6" height="70"/><rect x="52" y="20" width="6" height="90"/><rect x="64" y="55" width="6" height="55"/><rect x="76" y="35" width="6" height="75"/><rect x="88" y="66" width="6" height="44"/><rect x="100" y="28" width="6" height="82"/><rect x="112" y="46" width="6" height="64"/><rect x="124" y="18" width="6" height="92"/><rect x="136" y="58" width="6" height="52"/><rect x="148" y="38" width="6" height="72"/><rect x="160" y="24" width="6" height="86"/><rect x="172" y="50" width="6" height="60"/>
        </g>
      </svg>
      <div class="screen-row" style="color:#9aa1a6;font-weight:400"><span>Avg 11h 20m</span><span>Best 13h</span></div>
    </div>
  </div>
  <div class="feat-col feat-right">
    <div class="feat"><span class="feat-icon"><svg width="26" height="22" viewBox="0 0 26 22"><path d="M2 11h4M7 6v10M11 2v18M15 6v10M19 8v6M23 11h2" stroke="#fff" stroke-width="2"/></svg></span><div><h4>Breathing Movement</h4><p>Lorem ipsum is simply dummy text of the printing and typesetting</p></div></div>
    <div class="feat"><span class="feat-icon"><svg width="24" height="20" viewBox="0 0 24 20"><path d="M2 6h16l-4-4M22 14H6l4 4" stroke="#fff" stroke-width="2" fill="none"/></svg></span><div><h4>Fall Detection</h4><p>Lorem ipsum is simply dummy text of the printing and typesetting</p></div></div>
    <div class="feat"><span class="feat-icon"><svg width="22" height="24" viewBox="0 0 22 24"><path d="M11 1l9 4v7c0 6-4 10-9 11-5-1-9-5-9-11V5z" fill="#fff"/><path d="M7 12l3 3 5-6" stroke="#85cae6" stroke-width="2" fill="none"/></svg></span><div><h4>Proactive Monitoring</h4><p>Lorem ipsum is simply dummy text of the printing and typesetting</p></div></div>
  </div>
</section>

<section class="section video">
  <div class="ph video-photo" role="img" aria-label="Photo of a mother and baby sleeping peacefully side by side, with the Lunet sensor and charger nearby"></div>
  <h2 class="video-title">This smart monitor</h2>
  <p class="video-sub">actually helps you reclaim hours of much-needed sleep</p>
  <div class="cta">
    <span class="play"><svg width="16" height="18" viewBox="0 0 16 18"><path d="M2 1l13 8-13 8z" fill="#fff"/></svg></span>
    <a class="btn btn-blue">Watch Video</a>
  </div>
</section>

<section class="section get">
  <div class="get-band"></div>
  <h2 class="sec-title">Get the Lu<span class="accent">net</span> Tracker</h2>
  <p class="sec-sub">Starting at just $299.</p>
  <a class="btn btn-peach">Buy Lunet</a>
</section>

<section class="section about">
  <div class="ph about-photo" role="img" aria-label="Photo of a sleeping baby in a pink headband hugging a grey knitted teddy bear"></div>
  <div class="about-text">
    <h2>About Company</h2>
    <p>Corvane Tesk Digital builds gentle, affordable technology for new parents. Lorem ipsum is simply dummy text of the printing and typesetting industry, and has been the industry's standard dummy text ever since the 1500s, when an unknown printer took a galley of type and scrambled it to make a type specimen book.</p>
    <a class="btn btn-blue">About Us</a>
  </div>
</section>

<footer class="section footer">
  <div class="foot-cols">
    <div class="foot-col">Shipping &amp; Returns<br>Track Order<br>Find a Store<br>Contact<br>FAQ's</div>
    <div class="foot-col">Products Overview<br>Testimonials<br>Features</div>
    <div class="foot-col">Company<br>Reviews<br>Blog<br>Careers</div>
    <div class="foot-col foot-contact"><span class="phone-line">Call Us: 1-800-555-0142</span><br>e: hello@lunet-care.com<div class="social"><span></span><span></span><span></span></div></div>
  </div>
  <div class="foot-bottom">
    <span>© 2018 by Corvane Tesk Digital. All Rights Reserved.</span>
    <span class="legal"><span>Privacy</span><span>Terms Of Service</span><span>Warranty</span></span>
    <svg width="14" height="18" viewBox="0 0 14 18"><path d="M7 17V2M1 8l6-6 6 6" stroke="#85cae6" stroke-width="2" fill="none"/></svg>
  </div>
</footer>

</body>
</html>
```